Building Design company needing a letterhead

We need a letter head for our Building Design company to send letters etc. to our clients, consultants, councils etc. We would like to see our logo used and company colours. I have attached our style guide and an example of our current letterheads. Top left we would like our logo, top right we would like the company details and at the footer we would like some sort of image/design etc. that suits our brand. I like the Quarto Design letterhead attached.

Target Market(s)

Professionals, Councils, Consultants, Mums & Dads

Industry/Entity Type

Architecture

Font styles to use
Other font styles liked:
• refer the design style guide

Colors
f37122
000000
1b1b1b

Requirements
Must have
• Must have the minimum of a logo, company details and footer
Nice to have
• An image/design made for the footer that would suite our brand and website at www.tavorendesign.com.au. Also it would be nice to include the KMOTR logo somewhere perhaps included in the footer.
Should not have
• Large images in the header. I just want the logo and company details.

```html
<!DOCTYPE html>
<html lang="en">
<head>
<meta charset="utf-8">
<title>Tavoren Design Letterhead</title>
<link href="https://fonts.googleapis.com/css2?family=Arimo:wght@400;700&family=Roboto:wght@400;500&display=swap" rel="stylesheet">
<style>
  :root {
    --brand-orange: #f37122;
    --brand-black: #000000;
    --brand-ink: #1b1b1b;
    --brand-grey: #5a5452;
    --text-body: #2a2a2a;
    --stage: #ececee;
    --paper: #ffffff;
  }
  * { box-sizing: border-box; margin: 0; padding: 0; }
  html, body {
    width: 1200px; height: 1020px; overflow: hidden;
    background: var(--stage);
  }
  .letterhead {
    position: absolute; left: 260px; top: 30px;
    width: 679px; height: 960px;
    background: var(--paper);
    box-shadow: 0 2px 10px rgba(0,0,0,0.12);
    font-family: "Arimo", Arial, sans-serif;
    color: var(--text-body);
    overflow: hidden;
  }
  .contact-list {
    position: absolute; right: 70px; top: 44px;
    list-style: none;
    font-family: "Roboto", Arial, sans-serif;
    font-size: 11px; line-height: 15px; color: var(--brand-ink);
  }
  .contact-list li { display: flex; align-items: center; gap: 6px; }
  .contact-dot {
    width: 9px; height: 9px; border-radius: 50%;
    background: var(--brand-orange); flex: none;
  }
  .brand {
    position: absolute; left: 72px; top: 104px;
    display: flex; align-items: center; gap: 12px;
  }
  .brand-square { width: 30px; height: 30px; background: var(--brand-orange); }
  .brand-name {
    font-family: "Arimo", Arial, sans-serif; font-weight: 700;
    font-size: 30px; letter-spacing: 1.5px; color: var(--brand-ink);
    text-transform: uppercase;
  }
  .recipient {
    position: absolute; left: 72px; top: 210px;
    font-size: 11.5px; line-height: 15px; color: var(--brand-ink);
  }
  .recipient strong { font-weight: 700; }
  .letter-body {
    position: absolute; left: 100px; top: 290px; width: 500px;
    font-size: 11.5px; line-height: 16px; color: var(--text-body);
  }
  .letter-body p + p { margin-top: 18px; }
  .sign-off {
    position: absolute; left: 120px; top: 600px;
    font-size: 11.5px; font-weight: 700; color: var(--brand-ink);
  }
  .signature {
    width: 80px; height: 40px; margin: 8px 0 8px 30px;
    background: linear-gradient(135deg, #e9e9f0, #d6d6e2);
  }
  .sign-off .role { margin-left: 30px; }
  .footer-art { position: absolute; left: 0; top: 0; }
</style>
</head>
<body>
  <main class="letterhead">
    <ul class="contact-list">
      <li><span class="contact-dot"></span>(08) 6142 3380</li>
      <li><span class="contact-dot"></span>admin@tavorendesign.com.au</li>
      <li><span class="contact-dot"></span>www.tavorendesign.com.au</li>
    </ul>

    <div class="brand">
      <span class="brand-square"></span>
      <span class="brand-name">Tavoren Design</span>
    </div>

    <address class="recipient" style="font-style:normal">
      <strong>Lorem Ipsum</strong><br>
      Lorem Ipsum Admin<br>
      Street Name, City Name,<br>
      Zip Code - 00000
    </address>

    <section class="letter-body">
      <p>Lorem Ipsum is simply dummy text of the printing and typesetting industry. Lorem Ipsum has been the industry's standard dummy text ever since the 1500s, when an unknown printer took a galley of type and scrambled it to make a type specimen book. It has survived not only five centuries, but also the leap into electronic typesetting, remaining essentially unchanged.</p>
      <p>It was popularised in the 1960s with the release of Lettrafix sheets containing Lorem Ipsum passages, and more recently with desktop publishing software like Quill LayoutPro including versions of Lorem Ipsum.</p>
      <p>Contrary to popular belief, Lorem Ipsum is not simply random text. It has roots in a piece of classical Latin literature from 45 BC, making it over 2000 years old. Edmund Harrow, a Latin professor at Ashford-Linden College in Vermont, looked up one of the more obscure Latin words, consectetur, from a Lorem Ipsum passage, and going through the cites of the word in classical literature, discovered the undoubtable source.</p>
    </section>

    <div class="sign-off">
      <div>Lorem Ipsum</div>
      <div class="signature" role="img" aria-label="Handwritten signature"></div>
      <div class="role">Lorem Ipsum Admin</div>
    </div>

    <svg class="footer-art" width="679" height="960" viewBox="0 0 679 960" aria-hidden="false">
      <defs>
        <linearGradient id="footer-line" x1="0" y1="0" x2="1" y2="0">
          <stop offset="0" stop-color="#f37122"/>
          <stop offset="0.55" stop-color="#7a4a36"/>
          <stop offset="1" stop-color="#5a5452"/>
        </linearGradient>
      </defs>
      <line x1="0" y1="888" x2="679" y2="708" stroke="url(#footer-line)" stroke-width="5"/>
      <circle cx="592" cy="731" r="42" fill="#5a5452" role="img" aria-label="Partner membership badge"/>
      <g transform="rotate(-14.85 40 878)" font-family="Roboto, Arial, sans-serif" font-size="12">
        <circle cx="44" cy="868" r="5" fill="#f37122"/>
        <text x="56" y="872" fill="#1b1b1b">PO Box 1187 Halvern North WA 6999</text>
        <text x="56" y="900" fill="#1b1b1b"><tspan fill="#f37122">ABN</tspan> 31 402 118 764</text>
      </g>
    </svg>
  </main>
</body>
</html>
```